Zielgruppe
Wir machen individualisierte Biere mit entsprechend coolen Etiketten-Designs. In diesem Fall ist es ein Geschenk für einen Freund, der heiratet.
Aufgabenstellung
Er hat seiner Verlobten den Heiratsantrag unter Polarlichtern in Island gemacht. Es wäre cool, wenn man karrikativ zwei Menschen, die Hände halten unter Polarlichtern sieht und der oben genannte Name 'Drevic' auf Kyrillisch (serb. für Liebe) in den Polarlichtern integriert ist. Ich habe unten als Inspiration die Webseite der Bierbrauerei angegeben, dort seht ihr den Stil der anderen Designs. Das Etiketten-Format findet ihr im Anhang. Im Anhang findet ihr auch ein Bild von den Polarlichtern, wo er ihr den Heiratsantrag gemacht hat, vielleicht hilft es euch zur Vorstellung.
Website: https://vornelo.rs/shop/

```html
<!DOCTYPE html>
<html lang="sr">
<head>
<meta charset="utf-8">
<title>Древић – Etikett</title>
<link rel="stylesheet" href="https://fonts.googleapis.com/css2?family=Playfair+Display:wght@800&display=swap">
<style>
  :root {
    --page-bg: #f1f1ef;
    --label-bg: #ffffff;
    --label-edge: #e4e4e2;
    --title-fill: #c9cf9f;
    --title-shadow: #1d1f14;
    --heart-frame: #bcc48f;
    --sky-deep: #141a2a;
    --sky-green: #3f7a5e;
    --sky-violet: #6a4a78;
    --sky-ground: #0b0d14;
  }
  * { margin: 0; padding: 0; box-sizing: border-box; }
  html, body {
    width: 927px;
    height: 1200px;
    overflow: hidden;
    background: var(--page-bg);
  }
  .canvas {
    position: relative;
    width: 927px;
    height: 1200px;
  }
  .label {
    position: absolute;
    left: 111px;
    top: 50px;
    width: 705px;
    height: 1100px;
    background: var(--label-bg);
    border: 1px solid var(--label-edge);
  }
  .label-title {
    position: absolute;
    top: 70px;
    left: 0;
    width: 100%;
    text-align: center;
    font-family: "Playfair Display", serif;
    font-weight: 800;
    font-size: 168px;
    line-height: 1;
    color: var(--title-fill);
    -webkit-text-stroke: 5px var(--title-shadow);
    paint-order: stroke fill;
    text-shadow: 6px 6px 0 var(--title-shadow);
  }
  .heart {
    position: absolute;
    left: 0;
    top: 320px;
    width: 705px;
    height: 700px;
  }
</style>
</head>
<body>
<div class="canvas">
  <section class="label">
    <h1 class="label-title">древић</h1>
    <svg class="heart" viewBox="0 0 200 190" role="img" aria-label="Night sky with northern lights and the silhouette of a couple, one kneeling in a proposal">
      <defs>
        <linearGradient id="sky-base" x1="0" y1="0" x2="0" y2="1">
          <stop offset="0" stop-color="var(--sky-deep)"/>
          <stop offset="0.75" stop-color="#1b2233"/>
          <stop offset="1" stop-color="var(--sky-ground)"/>
        </linearGradient>
        <radialGradient id="aurora-green" cx="0.25" cy="0.3" r="0.45">
          <stop offset="0" stop-color="var(--sky-green)" stop-opacity="0.9"/>
          <stop offset="1" stop-color="var(--sky-green)" stop-opacity="0"/>
        </radialGradient>
        <radialGradient id="aurora-violet" cx="0.72" cy="0.35" r="0.45">
          <stop offset="0" stop-color="var(--sky-violet)" stop-opacity="0.9"/>
          <stop offset="1" stop-color="var(--sky-violet)" stop-opacity="0"/>
        </radialGradient>
        <clipPath id="heart-shape">
          <path d="M100 40 C100 40 80 2 45 6 C12 10 2 42 6 68 C12 108 60 140 100 184 C140 140 188 108 194 68 C198 42 188 10 155 6 C120 2 100 40 100 40 Z"/>
        </clipPath>
      </defs>
      <g clip-path="url(#heart-shape)">
        <rect width="200" height="190" fill="url(#sky-base)"/>
        <rect width="200" height="190" fill="url(#aurora-green)"/>
        <rect width="200" height="190" fill="url(#aurora-violet)"/>
      </g>
      <path d="M100 40 C100 40 80 2 45 6 C12 10 2 42 6 68 C12 108 60 140 100 184 C140 140 188 108 194 68 C198 42 188 10 155 6 C120 2 100 40 100 40 Z" fill="none" stroke="var(--heart-frame)" stroke-width="6" stroke-linejoin="round"/>
    </svg>
  </section>
</div>
</body>
</html>
```